New boutique hotel for tourists, with hint of art deco styling

This is a new, soon to be completed, boutique hotel in Sydney. A letterhead with a logo is required. Less emphasis on the word "boutique". Perhaps the word could be screened to be lighter in colour (or print intensity). Would like a simple, clear, easy-to read, sans serif type face. The information on the letterhead is:
Mrs Fennel Boutique Hotel
417 Larkmoor Street,
Wellbrook, NSW, 2094
Australia
Tel: +61 2 9704-5512
mrsfennelhotel@example-mail.com
mrsfennelhotel.example.au
ABN 47 902 365 148

Target Market(s)

travellers, tourists, various ages

Industry/Entity Type

Hospitality

Contact Information for Business Card

Mrs Fennel Boutique Hotel
417 Larkmoor Street,
Wellbrook, NSW, 2097
Telephone: (02) 9704-5512
www.mrsfennelhotel.example.au
mrsfennelhotel@example-mail.com
ABN 47 902 365 148

Logo Text

suggest playing with the letter "B"

Font styles to use
Sans Serif

Colors
3176b5

Requirements
Must have
• ABN to be very small.
• Must be clear, easy to read and in a sans serif typeface, please!
Nice to have
• The word "Boutique" should be less intense in appearance to the rest of the name, or even "Boutique Hotel" can have less prominence than "Mrs Fennel".
Should not have
• No serif typeface. Sans serif only will be accepted.

```html
<!DOCTYPE html>
<html lang="en">
<head>
<meta charset="utf-8">
<title>Mrs Fennel Boutique Hotel – Letterhead</title>
<link href="https://fonts.googleapis.com/css2?family=Tenor+Sans&display=swap" rel="stylesheet">
<style>
  :root {
    --brand-blue: #3176b5;
    --brand-blue-dark: #1f5f9e;
    --brand-blue-soft: #8fb5da;
    --backdrop: #a9cdf1;
    --paper: #f7fbff;
    --paper-tint: #e9f3fc;
    --mark-faint: #e6ecf7;
    --tile: #dcecfa;
    --contact-text: #4a7fb3;
  }
  * { box-sizing: border-box; margin: 0; padding: 0; }
  html, body {
    width: 1200px;
    height: 784px;
    overflow: hidden;
    background: var(--backdrop);
    font-family: "Tenor Sans", sans-serif;
  }
  .letterhead {
    position: absolute;
    left: 150px;
    top: 52px;
    width: 900px;
    height: 680px;
    background: linear-gradient(160deg, #ffffff 0%, var(--paper) 60%, var(--paper-tint) 100%);
    overflow: hidden;
  }
  .brand {
    position: absolute;
    top: 40px;
    left: 50%;
    transform: translateX(-50%);
    display: flex;
    flex-direction: column;
    align-items: center;
    gap: 6px;
    white-space: nowrap;
  }
  .brand-mark {
    display: flex;
    align-items: center;
    gap: 10px;
    color: var(--brand-blue);
    font-size: 22px;
    letter-spacing: 0.06em;
    text-transform: uppercase;
  }
  .brand-dot {
    width: 12px;
    height: 12px;
    border-radius: 50%;
    background: var(--brand-blue);
  }
  .brand-sub {
    color: var(--brand-blue-soft);
    font-size: 12px;
    letter-spacing: 0.2em;
    text-transform: uppercase;
  }
  .brand-watermark {
    position: absolute;
    top: 50%;
    left: 50%;
    transform: translate(-50%, -50%);
    color: var(--mark-faint);
    font-size: 64px;
    letter-spacing: 0.04em;
    white-space: nowrap;
  }
  .contact-tiles {
    position: absolute;
    right: 0;
    bottom: 0;
    width: 300px;
    height: 220px;
  }
  .contact {
    position: absolute;
    right: 40px;
    bottom: 36px;
    text-align: right;
    color: var(--brand-blue);
  }
  .contact-name {
    font-size: 14px;
    letter-spacing: 0.05em;
    margin-bottom: 8px;
    color: var(--brand-blue-dark);
    text-transform: uppercase;
  }
  .contact-name .name-sub { color: var(--brand-blue-soft); }
  .contact-line {
    display: flex;
    justify-content: flex-end;
    align-items: center;
    gap: 6px;
    font-size: 10px;
    letter-spacing: 0.04em;
    line-height: 16px;
    color: var(--contact-text);
  }
  .contact-line svg { width: 9px; height: 9px; flex: none; }
  .contact-abn {
    margin-top: 6px;
    font-size: 7px;
    letter-spacing: 0.06em;
    color: var(--brand-blue-soft);
  }
</style>
</head>
<body>
  <main class="letterhead">
    <header class="brand">
      <div class="brand-mark">
        <span class="brand-dot"></span>
        <span class="brand-name">Mrs Fennel</span>
      </div>
      <p class="brand-sub">Boutique Hotel</p>
    </header>

    <div class="brand-watermark" aria-hidden="true">Mrs Fennel</div>

    <svg class="contact-tiles" viewBox="0 0 300 220" aria-hidden="true">
      <rect x="150" y="20" width="70" height="60" fill="var(--tile)"/>
      <rect x="90" y="80" width="90" height="80" fill="var(--tile)" opacity="0.7"/>
      <rect x="200" y="100" width="100" height="120" fill="var(--tile)" opacity="0.55"/>
    </svg>

    <footer class="contact">
      <p class="contact-name">Mrs Fennel <span class="name-sub">Boutique Hotel</span></p>
      <p class="contact-line">
        <svg viewBox="0 0 10 10"><circle cx="5" cy="5" r="4.5" fill="var(--brand-blue)"/><path d="M5 2.2a1.8 1.8 0 0 0-1.8 1.8C3.2 5.4 5 7.8 5 7.8S6.8 5.4 6.8 4A1.8 1.8 0 0 0 5 2.2z" fill="#fff"/></svg>
        417 Larkmoor Street, Wellbrook, NSW, 2094
      </p>
      <p class="contact-line">Australia</p>
      <p class="contact-line">
        <svg viewBox="0 0 10 10"><circle cx="5" cy="5" r="4.5" fill="var(--brand-blue)"/><path d="M3.3 2.6l1 1-.5.7a4 4 0 0 0 1.9 1.9l.7-.5 1 1-.7.8C4.9 7.3 2.7 5.1 2.5 3.3z" fill="#fff"/></svg>
        Tel: +61 2 9704-5512
      </p>
      <p class="contact-line">
        <svg viewBox="0 0 10 10"><circle cx="5" cy="5" r="4.5" fill="var(--brand-blue)"/><rect x="2.5" y="3.2" width="5" height="3.6" fill="#fff"/><path d="M2.5 3.2L5 5.2 7.5 3.2" stroke="var(--brand-blue)" stroke-width="0.6" fill="none"/></svg>
        mrsfennelhotel@example-mail.com
      </p>
      <p class="contact-line">
        <svg viewBox="0 0 10 10"><circle cx="5" cy="5" r="4.5" fill="var(--brand-blue)"/><circle cx="5" cy="5" r="2.4" fill="none" stroke="#fff" stroke-width="0.7"/><path d="M2.6 5h4.8" stroke="#fff" stroke-width="0.6"/></svg>
        mrsfennelhotel.example.au
      </p>
      <p class="contact-abn">ABN 47 902 365 148</p>
    </footer>
  </main>
</body>
</html>
```